Construction training company needs a workshop invitation template

We need an invitation template for our professional development workshops we run for construction companies.
We would like to see designs that use the colors in our Timber Falcon Logo.
A simple, clean design with a lot of white space would be preferred.
No reverse text or italics.
The template should be done in Adobe Illustrator.

Requirements
Should not have
• Reverse text or italics

```html
<!DOCTYPE html>
<html lang="en">
<head>
<meta charset="utf-8">
<title>Timber Falcon Workshop Invitation</title>
<link rel="stylesheet" href="https://fonts.googleapis.com/css2?family=Arimo:wght@400;700&family=Cinzel:wght@700&family=Crimson+Pro:wght@400&display=swap">
<style>
  :root {
    --bg: #e9e9e9;
    --card: #f6f6f4;
    --ink: #4a3f3a;
    --green-light: #9bcb3f;
    --green: #6fae36;
    --green-dark: #4f8f2a;
    --rule: #c9c9c4;
    --drawing: #dcdcd8;
  }
  * { box-sizing: border-box; margin: 0; padding: 0; }
  html, body { width: 989px; height: 1200px; overflow: hidden; }
  body { background: var(--bg); font-family: "Arimo", Arial, sans-serif; color: var(--ink); position: relative; }

  .card {
    position: absolute; left: 170px; width: 650px; height: 460px;
    background: var(--card); overflow: hidden;
    box-shadow: 0 2px 6px rgba(0,0,0,.18);
  }
  .card--front { top: 70px; }
  .card--back { top: 610px; }

  .drawing-area {
    position: absolute; left: 0; bottom: 0; width: 170px; height: 170px;
    background: radial-gradient(ellipse at 20% 80%, var(--drawing), rgba(246,246,244,0) 70%);
  }

  .brand {
    position: absolute; left: 0; right: 0; display: flex; justify-content: center; align-items: center; gap: 10px;
  }
  .brand__mark { width: 22px; height: 22px; background: var(--green); }
  .brand__name { font-weight: 700; font-size: 17px; letter-spacing: 2px; text-transform: uppercase; color: var(--ink); }
  .card--front .brand { top: 52px; }
  .card--back .brand { top: 42px; }

  .headline {
    position: absolute; top: 128px; left: 0; right: 0; text-align: center;
    font-family: "Cinzel", "Times New Roman", serif; font-weight: 700; font-size: 40px;
    color: var(--green);
  }
  .center-text { position: absolute; left: 0; right: 0; text-align: center; }
  .invite-lead { top: 190px; font-size: 15px; line-height: 21px; }
  .invite-lead strong { font-size: 16px; }

  .pill {
    position: absolute; left: 50%; transform: translateX(-50%);
    height: 28px; border-radius: 14px; color: #fff; font-size: 14px;
    background: linear-gradient(90deg, var(--green-light), var(--green) 60%, var(--green-dark));
    display: flex; align-items: center; justify-content: center; white-space: nowrap;
    box-shadow: 0 4px 4px -2px rgba(79,143,42,.35);
  }
  .pill--date { top: 244px; width: 272px; }
  .pill--book { top: 380px; width: 502px; font-size: 14px; }
  .pill--book strong { margin-left: 4px; }

  .venue { top: 290px; font-size: 14px; }
  .case-study { top: 332px; font-size: 11px; line-height: 17px; }
  .more-info { top: 400px; font-size: 7.5px; }

  .intro { top: 104px; font-size: 13.5px; font-weight: 700; }

  .topics { position: absolute; top: 136px; list-style: none; width: 278px; }
  .topics--left { left: 38px; }
  .topics--right { left: 340px; }
  .topics li {
    font-family: "Crimson Pro", Georgia, serif; font-size: 11px; line-height: 12px;
    padding: 5px 0 5px 15px; border-bottom: 1px dotted var(--rule); position: relative; min-height: 23px;
  }
  .topics li::before {
    content: ""; position: absolute; left: 0; top: 7px; width: 8px; height: 8px; border-radius: 50%;
    background: var(--green);
  }
  .venue-small { top: 422px; font-size: 10px; }
</style>
</head>
<body>
  <section class="card card--front">
    <div class="drawing-area" role="img" aria-label="Faint architectural floor plan and building frame sketch"></div>
    <div class="brand"><span class="brand__mark"></span><span class="brand__name">Timber Falcon</span></div>
    <h1 class="headline">You’re Invited!</h1>
    <p class="center-text invite-lead">Ridgeway Builders invite you to a<br><strong>Timber Falcon Professional Development Workshop</strong></p>
    <div class="pill pill--date">Wednesday the 7th of June 2021</div>
    <p class="center-text venue">At [address of venue inserted here] 7200 AM to 12 noon</p>
    <p class="center-text case-study">The case study at this workshop will be the Ridgeway Builders<br>project at 14 Banksia Rd, Hillcrest<br>And there’s no charge for attending!</p>
    <p class="center-text more-info">See reverse side for more info...</p>
  </section>

  <section class="card card--back">
    <div class="drawing-area" role="img" aria-label="Faint architectural floor plan sketch"></div>
    <div class="brand"><span class="brand__mark"></span><span class="brand__name">Timber Falcon</span></div>
    <p class="center-text intro">This is a live action workshop where you participate in and learn about...</p>
    <ul class="topics topics--left">
      <li>How to set up a smart schedule for a construction project</li>
      <li>How to get clarity on the building work to be done, using a 3D model.</li>
      <li>Getting everybody onto the same page</li>
      <li>Solving construction headaches before they happen</li>
      <li>Getting the information you need to make you more efficient and effective</li>
      <li>How to get more satisfaction out of your work</li>
      <li>Delivering projects in less time and at lower costs</li>
      <li>Achieving better quality work</li>
    </ul>
    <ul class="topics topics--right">
      <li>Ensuring a high level of worksite safety</li>
      <li>Developing stronger relationships within the workforce</li>
      <li>How smart collaboration can improve things for everybody</li>
      <li>Transforming workplace culture and reducing the mental health issues in the construction industry</li>
      <li>Reducing rework and warranty work</li>
      <li>Creating better results, with less time, effort and cost</li>
      <li>Boosting customer satisfaction and referrals</li>
    </ul>
    <div class="pill pill--book">Seats are limited, so book your spot today! <strong>Call Maree on 0400 123 456</strong></div>
    <p class="center-text venue-small">At [address of venue inserted here] 7200 AM to 12 noon</p>
  </section>
</body>
</html>
```